Wealth Education Business Needs Sharp Business Card Design

We need a business card design for a recently launched investor education business called Harbor Crest.

The final design should promote security, empowerment, self improvement and financial gain. The card will ideally promote the stature of the business.

For more information and colours please visit harborcrest.com.au

Target Market(s)

Corporate executives and high net worth individuals

Industry/Entity Type

Education

Contact Information for Business Card

Name
Position
Contact Address
Phone
Mobile
Email
Website

```html
<!DOCTYPE html>
<html lang="en">
<head>
<meta charset="utf-8">
<title>Harbor Crest – Business Card</title>
<link href="https://fonts.googleapis.com/css2?family=Arimo:wght@400;700&display=swap" rel="stylesheet">
<style>
  :root {
    --backdrop-light: #9a9a9a;
    --backdrop-dark: #2e2e2e;
    --card: #ffffff;
    --ink: #3a3536;
    --divider: #5f8b8a;
    --teal: #6fb7b5;
    --sea: #7aa9a6;
    --green: #68c08a;
    --lime: #b8d88e;
    --mint: #d6eadf;
  }
  * { margin: 0; padding: 0; box-sizing: border-box; }
  html, body {
    width: 1200px; height: 846px; overflow: hidden;
  }
  body {
    position: relative;
    background: radial-gradient(ellipse 70% 75% at 50% 50%, var(--backdrop-light), var(--backdrop-dark));
    font-family: "Arimo", Arial, sans-serif;
    color: var(--ink);
  }
  .card {
    position: absolute;
    width: 603px; height: 344px;
    background: var(--card);
    overflow: hidden;
  }
  .card--front { left: 298px; top: 66px; }
  .card--back { left: 299px; top: 436px; }

  .accent-area {
    position: absolute;
    left: 0; top: 152px;
    width: 222px; height: 192px;
    background: linear-gradient(90deg, rgba(111,183,181,.55), rgba(104,192,138,.45) 55%, rgba(184,216,142,.4));
    clip-path: polygon(0 0, 35% 20%, 65% 40%, 100% 62%, 100% 100%, 0 100%);
  }

  .identity {
    position: absolute;
    right: 370px; top: 84px;
    text-align: left;
  }
  .identity__name { font-size: 26px; font-weight: 700; line-height: 30px; }
  .identity__position { font-size: 20px; line-height: 24px; }

  .divider {
    position: absolute;
    left: 268px; top: 68px;
    width: 5px; height: 226px;
    background: var(--divider);
  }

  .contact {
    position: absolute;
    left: 317px; top: 118px;
    list-style: none;
    font-size: 20px; line-height: 24px;
  }

  .brand-mini {
    position: absolute;
    right: 30px; top: 30px;
    display: flex; align-items: center; gap: 8px;
    font-size: 16px; letter-spacing: 1px;
    color: var(--ink);
  }
  .brand-mini__dot {
    width: 12px; height: 12px; border-radius: 50%;
    background: var(--teal);
  }

  .brand {
    position: absolute;
    left: 0; right: 0; top: 150px;
    text-align: center;
    font-size: 40px; line-height: 44px;
    letter-spacing: 9px;
    color: var(--ink);
  }
</style>
</head>
<body>
  <section class="card card--front">
    <div class="accent-area" role="img" aria-label="Decorative cluster of rounded teal and green bars"></div>

    <div class="identity">
      <p class="identity__name">Name</p>
      <p class="identity__position">Position</p>
    </div>

    <div class="divider"></div>

    <ul class="contact">
      <li>Contact</li>
      <li>Address</li>
      <li>Phone</li>
      <li>Mobile</li>
      <li>Email</li>
      <li>Website</li>
    </ul>

    <div class="brand-mini">
      <span class="brand-mini__dot"></span>
      <span>Harbor Crest</span>
    </div>
  </section>

  <section class="card card--back">
    <p class="brand">HARBOR CREST</p>
  </section>
</body>
</html>
```